Real Estate Company Website

We are working with ZP Real Estate and building a new website for them.
Some sites to use for content/competitors and inspiration:
https://doranpeltz.vq.com
https://www.dwellorix.com
https://www.mansard47.com
https://delphinetorsby.com
https://ottiliefrenz.com
https://simonpellor.com
https://noraquistelgroup.com
Thank you for taking the time to consider designing a website for us. We are web developers based in Stockton, CA, USA. Most of our projects go through the same process. Understanding this process may help you win a project with us. We custom-code all of our websites in-house. We don’t have any requirements as to what tools you use for your design, but we prefer Figma files. For any design that we label as four stars, we send it to the client for review. The client picks the final design they want us to use. Once we complete this process, we will continue to show additional clients all the four-star sites and purchase them later. Your designs will have multiple chances to sell. For better chances of success, we ask that you follow these guidelines.
IMAGES:
If you use any images or icons in the design, we ask that you have a link to the asset so we can purchase the image/icon. Most of the designs we submit do not have the customer’s images on them unless they have some great images. Be creative; show us the feeling you are trying to portray with your image choices. Use any royalty-free site you choose. We subscribe to Vexlo and mainly use their images, but we can purchase images outside of Vexlo. PLEASE NOTE: we will not submit designs to clients with watermarks on the images.
FONTS:
We ask that you identify the fonts used in the design. This can be done in a message if you want. We typically use Nubrik Fonts and Vexlo Fonts.
CONTENT:
We're always open to different content and ideas. We often submit designs with stock images so the client can see our vision. We typically take pictures after the website launch to use their images with our vision. Lorem Ipsum is fine for paragraphs, but we ask that you write the headers in correct English. We want to be able to show the vision and identify the sections of the website.
INSPIRATION:
We typically add a couple of links in the brief of websites we like to help you get started in your design.
REVISIONS:
We do not often ask for revisions of the designs unless we see something in the design that may not appeal to the client. If there are slight changes that we want to make, we do that in the development process.
FEEDBACK:
We rarely give feedback on designs during the design process. We are working on many website projects and do not have the time to provide feedback. We usually respond if your request is well thought out and asks specific questions, but a note asking “feedback, please” usually goes unanswered.

```html
<!DOCTYPE html>
<html lang="en">
<head>
<meta charset="utf-8">
<title>ZP Real Estate</title>
<link href="https://fonts.googleapis.com/css2?family=Merriweather:wght@400;700&family=Lato:wght@400;700&display=swap" rel="stylesheet">
<style>
:root{
  --teal:#175d6e;
  --teal-dark:#12495a;
  --ink:#1a1a1a;
  --muted:#7a7a7a;
  --mist:#eef4f4;
  --line:#2b2b2b;
  --white:#fff;
  --black:#000;
}
*{box-sizing:border-box;margin:0;padding:0}
html,body{width:1200px;height:3915px;overflow:hidden}
body{position:relative;font-family:'Lato',sans-serif;color:var(--ink);background:var(--white)}
.abs{position:absolute}
.serif{font-family:'Merriweather',serif}

/* top bar */
.topbar{left:0;top:0;width:1200px;height:43px;background:var(--teal);color:#fff;font-size:15px}
.topbar .item{top:12px;display:flex;align-items:center;gap:10px}
.social-dot{width:12px;height:12px;border:1.5px solid #fff;border-radius:50%}

/* nav */
.nav{left:0;top:43px;width:1200px;height:85px;background:#fff}
.brand{left:99px;top:24px;font-family:'Merriweather',serif;font-weight:700;font-size:22px;color:var(--ink);display:flex;align-items:center;gap:10px}
.brand .sq{width:22px;height:22px;background:var(--teal)}
.menu{right:100px;top:32px;display:flex;gap:37px;font-family:'Merriweather',serif;font-size:16px;color:#222}
.menu .active{color:var(--teal);border-bottom:2px solid var(--teal);padding-bottom:3px}

/* hero */
.hero{left:0;top:128px;width:1200px;height:601px;background:linear-gradient(180deg,#3c4658 0%,#4a5566 40%,#4d5e3e 75%,#3f5a2c 100%)}
.hero-title{left:0;width:1200px;top:166px;text-align:center;font-family:'Merriweather',serif;font-weight:700;font-size:55px;color:#fff}
.hero-rule{left:565px;top:242px;width:70px;height:4px;background:#fff}
.tabs{left:0;width:1200px;top:268px;display:flex;justify-content:center;gap:0}
.tab{display:flex;flex-direction:column;align-items:center;color:#fff;font-size:19px;margin:0 14px}
.tab .ic{width:38px;height:38px;border-radius:50%;background:rgba(255,255,255,.35);display:flex;align-items:center;justify-content:center;margin-bottom:12px}
.tab.on .ic{background:var(--teal);border:2px solid #fff}
.tab.on span{font-weight:700;border-bottom:3px solid #fff;padding-bottom:6px}
.search{left:297px;top:392px;width:608px;height:41px;background:#fff;border-radius:21px;font-size:14px;color:#aaa;padding:12px 0 0 28px}
.search .go{position:absolute;right:6px;top:6px;width:29px;height:29px;border-radius:50%;background:var(--teal)}
.hero-arrow{top:272px}

/* featured */
.featured{left:0;top:729px;width:1200px;height:652px;background:var(--mist)}
.sec-title{left:0;width:1200px;text-align:center;font-family:'Merriweather',serif;font-weight:700;font-size:34px;color:var(--ink)}
.sec-title em{font-style:normal;color:var(--teal)}
.sub{left:0;width:1200px;top:142px;text-align:center;font-size:16px}
.card{top:190px;width:312px;height:374px;background:#fff;border-radius:12px;overflow:hidden;box-shadow:0 2px 8px rgba(0,0,0,.06)}
.card .photo{height:193px}
.badge{position:absolute;right:20px;top:17px;background:#fff;border-radius:12px;padding:3px 18px;font-size:14px}
.card .body{padding:16px 17px}
.price{font-size:21px}
.heart{position:absolute;right:14px;top:211px;width:32px;height:32px;border-radius:50%;background:#e4eeee;display:flex;align-items:center;justify-content:center}
.specs{font-size:16px;margin-top:6px;color:#333}
.specs b{font-weight:400;color:#111}
.addr{font-size:15px;margin-top:14px;padding-left:2px}
.blurb{font-size:13px;color:var(--muted);margin-top:8px;line-height:24px}
.round-arrow{width:40px;height:40px;border-radius:50%;background:#fff;display:flex;align-items:center;justify-content:center;box-shadow:0 1px 4px rgba(0,0,0,.1)}

/* about */
.about-h{left:99px;top:1466px;font-family:'Merriweather',serif;font-weight:700;font-size:33px;line-height:40px}
.about-h em{font-style:normal;color:var(--teal)}
.about-rule{left:99px;top:1568px;width:50px;height:3px;background:var(--teal)}
.about-lead{left:99px;top:1584px;width:340px;font-size:16px;line-height:31px}
.about-copy{left:503px;top:1464px;width:600px;font-size:14px;line-height:31px;color:#333}
.about-photo{left:99px;top:1684px;width:1002px;height:490px;border-radius:12px;background:linear-gradient(180deg,#b9c8cf 0%,#c0574a 28%,#d9cdb6 55%,#6b7d4a 85%,#8a8578 100%)}

/* inventory */
.inv-rule{left:574px;top:2299px;width:52px;height:3px;background:var(--teal)}
.tile{width:321px;height:238px;border-radius:8px;overflow:hidden}
.tile .cap{position:absolute;left:24px;bottom:18px;color:#fff;font-weight:700;font-size:15px}
.tile .cap:before{content:"";position:absolute;left:0;top:-10px;width:40px;height:2px;background:#fff}
.tile .go{position:absolute;right:22px;bottom:14px;width:30px;height:30px;border-radius:50%;background:#fff;display:flex;align-items:center;justify-content:center}

/* downloads */
.dl{left:99px;width:591px;height:40px}
.dl h3{position:absolute;left:0;top:0;font-family:'Merriweather',serif;font-weight:700;font-size:27px}
.dl .link{position:absolute;right:18px;top:8px;font-size:13px;display:flex;align-items:center;gap:8px;letter-spacing:.2px}
.dl-line{left:99px;width:591px;height:1px;background:var(--line)}
.portrait{left:690px;top:2919px;width:414px;height:584px;border-radius:207px 207px 0 0;background:linear-gradient(180deg,#d8d2c8 0%,#cfc6b8 45%,#b9b4ad 100%)}

/* footer */
.footer{left:0;top:3593px;width:1200px;height:282px;background:var(--black);color:#fff}
.f-brand{left:110px;top:90px;font-family:'Merriweather',serif;font-weight:700;font-size:30px;display:flex;align-items:center;gap:12px}
.f-brand .sq{width:26px;height:26px;background:#fff}
.f-head{font-weight:700;font-size:17px;display:flex;align-items:center;gap:12px}
.f-text{font-size:16px}
.ql{left:969px;top:63px}
.ql ul{list-style:none;margin-top:24px}
.ql li{font-size:15px;height:31px;display:flex;align-items:center;gap:18px}
.ql li:before{content:"";border-left:6px solid #fff;border-top:5px solid transparent;border-bottom:5px solid transparent}
.bottombar{left:0;top:3875px;width:1200px;height:40px;background:var(--teal);color:#fff;font-size:15px}
</style>
</head>
<body>

<header class="abs topbar">
  <div class="abs item" style="left:99px">
    <svg width="14" height="14" viewBox="0 0 24 24" fill="#fff"><path d="M6.6 10.8a15 15 0 0 0 6.6 6.6l2.2-2.2c.3-.3.7-.4 1-.2 1.1.4 2.3.6 3.6.6.6 0 1 .4 1 1V20c0 .6-.4 1-1 1A17 17 0 0 1 3 4c0-.6.4-1 1-1h3.5c.6 0 1 .4 1 1 0 1.3.2 2.5.6 3.6.1.3 0 .7-.2 1z"/></svg>
    +1 555 014 7788
  </div>
  <div class="abs item" style="left:313px">
    <svg width="16" height="12" viewBox="0 0 24 18" fill="#fff"><path d="M0 0h24v18H0z" opacity="0"/><path d="M2 0h20a2 2 0 0 1 2 2v.5L12 10 0 2.5V2a2 2 0 0 1 2-2zm-2 5l12 7.5L24 5v11a2 2 0 0 1-2 2H2a2 2 0 0 1-2-2z"/></svg>
    hello@zprealestate.com
  </div>
  <div class="abs item" style="left:1008px;top:15px"><span class="social-dot"></span></div>
  <div class="abs" style="left:1042px;top:12px;opacity:.6">|</div>
  <div class="abs item" style="left:1064px;top:13px">
    <svg width="18" height="18" viewBox="0 0 24 24" fill="none" stroke="#fff" stroke-width="1.8"><circle cx="12" cy="12" r="9"/><path d="M3 12h18M12 3c3 3 3 15 0 18M12 3c-3 3-3 15 0 18"/></svg>
    <svg width="10" height="8" viewBox="0 0 10 6" fill="none" stroke="#fff" stroke-width="1.6"><path d="M1 1l4 4 4-4"/></svg>
  </div>
</header>

<nav class="abs nav">
  <div class="abs brand"><span class="sq"></span>ZP Real Estate</div>
  <div class="abs menu">
    <span class="active">Home</span><span>About Us</span><span>Properties</span><span>Home Search</span><span>Blog</span><span>Contact Us</span>
  </div>
</nav>

<section class="abs hero" role="img" aria-label="Photo of a blue two-storey house with a stone path and lawn at dusk">
  <h1 class="abs hero-title">Let's find your dream home</h1>
  <div class="abs hero-rule"></div>
  <div class="abs tabs">
    <div class="tab on"><div class="ic"><svg width="18" height="18" viewBox="0 0 24 24" fill="none" stroke="#fff" stroke-width="2"><path d="M3 11l9-7 9 7v9H3z"/></svg></div><span>Buy</span></div>
    <div class="tab"><div class="ic"><svg width="18" height="18" viewBox="0 0 24 24" fill="none" stroke="#fff" stroke-width="2"><path d="M3 11l9-7 9 7v9H3z"/></svg></div><span>Rent</span></div>
    <div class="tab"><div class="ic"><svg width="18" height="18" viewBox="0 0 24 24" fill="none" stroke="#fff" stroke-width="2"><path d="M3 11l9-7 9 7v9H3z"/></svg></div><span>Sell</span></div>
    <div class="tab"><div class="ic"><svg width="18" height="18" viewBox="0 0 24 24" fill="none" stroke="#fff" stroke-width="2"><path d="M3 11l9-7 9 7v9H3z"/><circle cx="12" cy="14" r="3"/></svg></div><span>Pre-approval</span></div>
    <div class="tab"><div class="ic"><svg width="18" height="18" viewBox="0 0 24 24" fill="none" stroke="#fff" stroke-width="2"><path d="M3 11l9-7 9 7v9H3z"/><path d="M9 14l2 2 4-4"/></svg></div><span>Just sold</span></div>
    <div class="tab"><div class="ic"><svg width="18" height="18" viewBox="0 0 24 24" fill="none" stroke="#fff" stroke-width="2"><path d="M3 11l9-7 9 7v9H3z"/><path d="M12 11v6"/></svg></div><span>Home value</span></div>
  </div>
  <div class="abs search">Address, School, City, Zip or Neighborhood
    <span class="go"><svg width="29" height="29" viewBox="0 0 29 29" fill="none" stroke="#fff" stroke-width="2"><circle cx="13.5" cy="13.5" r="4.5"/><path d="M17 17l3 3"/></svg></span>
  </div>
  <svg class="abs hero-arrow" style="left:40px" width="30" height="60" viewBox="0 0 30 60" fill="none" stroke="#fff" stroke-width="2"><path d="M28 2L2 30l26 28"/></svg>
  <svg class="abs hero-arrow" style="left:1130px" width="30" height="60" viewBox="0 0 30 60" fill="none" stroke="#fff" stroke-width="2"><path d="M2 2l26 28L2 58"/></svg>
</section>

<section class="abs featured">
  <h2 class="abs sec-title" style="top:72px">Featured <em>Properties</em></h2>
  <p class="abs sub">Check out my featured properties.</p>

  <div class="abs round-arrow" style="left:24px;top:358px"><svg width="12" height="12" viewBox="0 0 10 10" fill="none" stroke="var(--teal)" stroke-width="1.6"><path d="M7 1L3 5l4 4"/></svg></div>
  <div class="abs round-arrow" style="left:1136px;top:358px"><svg width="12" height="12" viewBox="0 0 10 10" fill="none" stroke="var(--teal)" stroke-width="1.6"><path d="M3 1l4 4-4 4"/></svg></div>

  <article class="abs card" style="left:99px">
    <div class="photo" role="img" aria-label="Photo of a grey two-storey house with a driveway" style="background:linear-gradient(180deg,#9fb0bd,#6c6f6e 60%,#5d6a45)"></div>
    <span class="badge">Sale</span>
    <span class="heart"><svg width="16" height="14" viewBox="0 0 24 21" fill="none" stroke="var(--teal)" stroke-width="2.4"><path d="M12 19S2 13 2 7a5 5 0 0 1 10-1 5 5 0 0 1 10 1c0 6-10 12-10 12z"/></svg></span>
    <div class="body">
      <div class="price">$836,000</div>
      <div class="specs"><b>4</b> bd <b>3.0</b> ba <b>2,156</b> sq ft <b>0.18</b> ac</div>
      <div class="addr">2817 Cedar Hollow Road, Lake Verna</div>
      <div class="blurb">Lorem ipsum dolor sit consectetur adipiscing elit eiusmod tempor</div>
    </div>
  </article>
  <article class="abs card" style="left:444px">
    <div class="photo" role="img" aria-label="Photo of a family walking toward a grey house" style="background:linear-gradient(180deg,#a89a7e,#6d6a60 55%,#6f6a4a)"></div>
    <span class="badge">Sale</span>
    <span class="heart"><svg width="16" height="14" viewBox="0 0 24 21" fill="none" stroke="var(--teal)" stroke-width="2.4"><path d="M12 19S2 13 2 7a5 5 0 0 1 10-1 5 5 0 0 1 10 1c0 6-10 12-10 12z"/></svg></span>
    <div class="body">
      <div class="price">$836,000</div>
      <div class="specs"><b>4</b> bd <b>3.0</b> ba <b>2,156</b> sq ft <b>0.18</b> ac</div>
      <div class="addr">2817 Cedar Hollow Road, Lake Verna</div>
      <div class="blurb">Lorem ipsum dolor sit consectetur adipiscing elit eiusmod tempor</div>
    </div>
  </article>
  <article class="abs card" style="left:789px">
    <div class="photo" role="img" aria-label="Photo of a large grey house with a teal door and lawn" style="background:linear-gradient(180deg,#7fa3c8,#7e8a90 55%,#5c7a3e)"></div>
    <span class="badge">Sale</span>
    <span class="heart"><svg width="16" height="14" viewBox="0 0 24 21" fill="none" stroke="var(--teal)" stroke-width="2.4"><path d="M12 19S2 13 2 7a5 5 0 0 1 10-1 5 5 0 0 1 10 1c0 6-10 12-10 12z"/></svg></span>
    <div class="body">
      <div class="price">$836,000</div>
      <div class="specs"><b>4</b> bd <b>3.0</b> ba <b>2,156</b> sq ft <b>0.18</b> ac</div>
      <div class="addr">2817 Cedar Hollow Road, Lake Verna</div>
      <div class="blurb">Lorem ipsum dolor sit consectetur adipiscing elit eiusmod tempor</div>
    </div>
  </article>
</section>

<section>
  <h2 class="abs about-h">About<br><em>ZP Real Estate</em></h2>
  <div class="abs about-rule"></div>
  <p class="abs about-lead">Lorem ipsum dolor sit amet, consectetur adipiscing elit, sed do incididunt labore</p>
  <p class="abs about-copy">Lorem ipsum dolor sit amet, consectetur adipiscing elit, sed do eiusmod tempor incididunt ut labore et dolore magna aliqua. Ut enim ad minim veniam, quis nostrud exercitation ullamco laboris nisi ut aliquip ex ea commodo consequat. Duis aute irure dolor in reprehenderit in voluptate velit esse cillum dolore eu fugiat nulla pariatur. Excepteur sint occaecat cupidatat non proident, sunt in culpa qui officia deserunt laborum.</p>
  <div class="abs about-photo" role="img" aria-label="Photo of a brick bungalow with a red roof, porch columns and garden"></div>
</section>

<section>
  <h2 class="abs sec-title" style="top:2250px">Current <em>Inventory</em></h2>
  <div class="abs inv-rule"></div>

  <div class="abs tile" style="left:99px;top:2333px;background:linear-gradient(180deg,#e8e6e2,#9a8f82)" role="img" aria-label="Photo of a couple celebrating in a new home among moving boxes"><span class="cap">LOREM IPSUM DOLOR</span><span class="go"><svg width="10" height="10" viewBox="0 0 10 10" fill="none" stroke="#333" stroke-width="1.6"><path d="M3 1l4 4-4 4"/></svg></span></div>
  <div class="abs tile" style="left:439px;top:2333px;background:linear-gradient(180deg,#c9c2b6,#5e5247)" role="img" aria-label="Photo of a modern living room interior"><span class="cap">LOREM IPSUM DOLOR</span><span class="go"><svg width="10" height="10" viewBox="0 0 10 10" fill="none" stroke="#333" stroke-width="1.6"><path d="M3 1l4 4-4 4"/></svg></span></div>
  <div class="abs tile" style="left:779px;top:2333px;background:linear-gradient(180deg,#5f8fc6,#8a7a68 60%,#6c7650)" role="img" aria-label="Photo of a two-storey house with a double garage"><span class="cap">LOREM IPSUM DOLOR</span><span class="go"><svg width="10" height="10" viewBox="0 0 10 10" fill="none" stroke="#333" stroke-width="1.6"><path d="M3 1l4 4-4 4"/></svg></span></div>
  <div class="abs tile" style="left:99px;top:2593px;background:linear-gradient(180deg,#bfb3a3,#5c4a3c)" role="img" aria-label="Photo of a family sitting together on a sofa"><span class="cap">LOREM IPSUM DOLOR</span><span class="go"><svg width="10" height="10" viewBox="0 0 10 10" fill="none" stroke="#333" stroke-width="1.6"><path d="M3 1l4 4-4 4"/></svg></span></div>
  <div class="abs tile" style="left:439px;top:2593px;background:linear-gradient(180deg,#b9bec4,#e2e2e0 55%,#55623c)" role="img" aria-label="Photo of a white house with dark shutters and trees"><span class="cap">LOREM IPSUM DOLOR</span><span class="go"><svg width="10" height="10" viewBox="0 0 10 10" fill="none" stroke="#333" stroke-width="1.6"><path d="M3 1l4 4-4 4"/></svg></span></div>
  <div class="abs tile" style="left:779px;top:2593px;background:linear-gradient(180deg,#e4e1dc,#8b8f96)" role="img" aria-label="Photo of a woman relaxing on a sofa at home"><span class="cap">LOREM IPSUM DOLOR</span><span class="go"><svg width="10" height="10" viewBox="0 0 10 10" fill="none" stroke="#333" stroke-width="1.6"><path d="M3 1l4 4-4 4"/></svg></span></div>
</section>

<section>
  <div class="abs dl" style="top:3022px"><h3>Lorem Lpsum</h3><span class="link">DOWNLOAD LOREM LPSUM <svg width="40" height="14" viewBox="0 0 40 14" fill="none" stroke="#111" stroke-width="2"><path d="M0 7h37M31 1l6 6-6 6"/></svg></span></div>
  <div class="abs dl-line" style="top:3086px"></div>
  <div class="abs dl" style="top:3127px"><h3>Long Bio</h3><span class="link">DOWNLOAD LONG BIO <svg width="40" height="14" viewBox="0 0 40 14" fill="none" stroke="#111" stroke-width="2"><path d="M0 7h37M31 1l6 6-6 6"/></svg></span></div>
  <div class="abs dl-line" style="top:3191px"></div>
  <div class="abs dl" style="top:3232px"><h3>Short Bio</h3><span class="link">DOWNLOAD SHORT BIO <svg width="40" height="14" viewBox="0 0 40 14" fill="none" stroke="#111" stroke-width="2"><path d="M0 7h37M31 1l6 6-6 6"/></svg></span></div>
  <div class="abs dl-line" style="top:3296px"></div>
  <div class="abs dl" style="top:3337px"><h3>Stage Intro</h3><span class="link">DOWNLOAD STAGE INTRO <svg width="40" height="14" viewBox="0 0 40 14" fill="none" stroke="#111" stroke-width="2"><path d="M0 7h37M31 1l6 6-6 6"/></svg></span></div>
  <div class="abs dl-line" style="top:3401px"></div>
  <div class="abs dl" style="top:3442px"><h3>One Sheeter</h3><span class="link">DOWNLOAD ONE SHEETER <svg width="40" height="14" viewBox="0 0 40 14" fill="none" stroke="#111" stroke-width="2"><path d="M0 7h37M31 1l6 6-6 6"/></svg></span></div>
  <div class="abs portrait" role="img" aria-label="Portrait of the agent in a light blazer holding a tablet"></div>
</section>

<footer class="abs footer">
  <div class="abs f-brand"><span class="sq"></span>ZP Real Estate</div>
  <div class="abs f-head" style="left:110px;top:237px">
    <svg width="16" height="16" viewBox="0 0 24 24" fill="#fff"><path d="M6.6 10.8a15 15 0 0 0 6.6 6.6l2.2-2.2c.3-.3.7-.4 1-.2 1.1.4 2.3.6 3.6.6.6 0 1 .4 1 1V20c0 .6-.4 1-1 1A17 17 0 0 1 3 4c0-.6.4-1 1-1h3.5c.6 0 1 .4 1 1 0 1.3.2 2.5.6 3.6.1.3 0 .7-.2 1z"/></svg>
    EMAIL: <span style="font-weight:400">hello@zprealestate.com</span>
  </div>
  <div class="abs f-head" style="left:572px;top:63px">
    <svg width="16" height="22" viewBox="0 0 16 22" fill="#fff"><path d="M8 0a8 8 0 0 1 8 8c0 6-8 14-8 14S0 14 0 8a8 8 0 0 1 8-8zm0 5a3 3 0 1 0 0 6 3 3 0 0 0 0-6z"/></svg>
    CONTACT US:
  </div>
  <div class="abs f-text" style="left:572px;top:112px;line-height:34px">ZP Real Estate<br>742 Harbor Crest Lane<br>Stockton, CA 95207</div>
  <div class="abs f-head" style="left:572px;top:237px">
    <svg width="16" height="16" viewBox="0 0 24 24" fill="#fff"><path d="M6.6 10.8a15 15 0 0 0 6.6 6.6l2.2-2.2c.3-.3.7-.4 1-.2 1.1.4 2.3.6 3.6.6.6 0 1 .4 1 1V20c0 .6-.4 1-1 1A17 17 0 0 1 3 4c0-.6.4-1 1-1h3.5c.6 0 1 .4 1 1 0 1.3.2 2.5.6 3.6.1.3 0 .7-.2 1z"/></svg>
    PHONE: <span style="font-weight:400">+1 555 014 7788</span>
  </div>
  <div class="abs ql">
    <div class="f-head">QUICK LINKS:</div>
    <ul><li>Home</li><li>About Us</li><li>Properties</li><li>Blog</li><li>Contact Us</li></ul>
  </div>
</footer>

<div class="abs bottombar">
  <span class="abs" style="left:110px;top:10px">2024 ZP Real Estate. All Rights Reserved.</span>
  <span class="abs social-dot" style="left:1073px;top:14px;width:14px;height:14px"></span>
</div>

</body>
</html>
```